依頼詳細
ゴミ屋敷の片づけ・遺品整理等の事業になります。
ポスティングを想定しています。
ターゲットは高齢者になりますのでわかりやすいデザインでお願いします。
記載項目
屋号:そよかぜクリーンサービス
電話番号:未定
サイズ
A4
ページ数
両面
希望イメージ
シンプル 複雑
単色 カラフル
暗い 明るい
日常 高級
遊び心 厳粛
未来的 伝統的
女性的 男性的
希望する色
緑系
納品ファイル
• 高解像度JPG (.jpg)
補足説明
■ 選んだ理由

高齢者向けということでイラストを多用しわかりやすいデザインで気に入りました。
ベースもやさしめの色合いで好きです。

■ 提案者全員のお礼・コメント

さまざまな提案をいただき感謝しています。ありがとうございました。

```html
<!DOCTYPE html>
<html lang="ja">
<head>
<meta charset="UTF-8">
<title>そよかぜクリーンサービス</title>
<link href="https://fonts.googleapis.com/css2?family=Noto+Serif+JP:wght@400;600;700&family=Noto+Sans+JP:wght@400;500;700&display=swap" rel="stylesheet">
<style>
  :root {
    --green: #5a9e2f;
    --green-light: #8cc63f;
    --green-dark: #3f7d1f;
    --text: #333333;
    --white: #ffffff;
    --photo-a: #e9ddd6;
    --photo-b: #c9b7ae;
  }
  * { margin: 0; padding: 0; box-sizing: border-box; }
  html, body { width: 849px; height: 1200px; overflow: hidden; background: var(--white); }
  .flyer {
    position: relative; width: 849px; height: 1200px; overflow: hidden;
    background: var(--white);
    font-family: "Noto Sans JP", sans-serif; color: var(--text);
  }
  .hero-photo {
    position: absolute; left: 0; top: 0; width: 849px; height: 420px;
    background: radial-gradient(ellipse at 70% 40%, #f7efe9 0%, var(--photo-a) 45%, var(--photo-b) 100%);
  }
  .hero-photo::after {
    content: ""; position: absolute; left: 0; right: 0; bottom: 0; height: 140px;
    background: linear-gradient(to bottom, rgba(255,255,255,0), var(--white));
  }
  .hero-lead {
    position: absolute; left: 100px; top: 136px;
    font-family: "Noto Serif JP", serif; font-size: 27px; color: var(--white);
    letter-spacing: 2px; text-shadow: 0 0 6px rgba(0,0,0,.25);
  }
  .hero-title {
    position: absolute; left: 56px; top: 180px;
    font-family: "Noto Serif JP", serif; font-weight: 600; font-size: 58px; line-height: 1.22;
    color: var(--white); letter-spacing: 2px; text-shadow: 0 0 8px rgba(0,0,0,.3);
  }
  .bubble {
    position: absolute; border-radius: 50%; padding: 0 16px;
    background: radial-gradient(circle at 40% 35%, var(--green-light) 0%, var(--green) 75%, var(--green-dark) 100%);
    color: var(--white); display: flex; flex-direction: column; justify-content: center; align-items: center;
    text-align: center; font-size: 14px; line-height: 1.6; font-weight: 500;
    box-shadow: 0 3px 8px rgba(0,0,0,.15);
  }
  .bubble .heading { font-size: 14px; margin-bottom: 2px; white-space: nowrap; }
  .bubble-items { text-align: left; }
  .bubble--memorial { left: 307px; top: 335px; width: 236px; height: 236px; font-size: 13px; }
  .bubble--home { left: 116px; top: 446px; width: 220px; height: 220px; font-size: 13px; }
  .bubble--storage { left: 554px; top: 458px; width: 220px; height: 220px; font-size: 13px; }
  .bubble--storage .heading { font-size: 12px; letter-spacing: -0.5px; }
  .bubble--more { left: 294px; top: 578px; width: 262px; height: 262px; font-size: 24px; line-height: 1.55; font-family: "Noto Serif JP", serif; }
  .message {
    position: absolute; left: 0; right: 0; top: 898px; text-align: center;
    font-family: "Noto Serif JP", serif; font-size: 22px; line-height: 1.55; color: var(--text);
  }
  .company {
    position: absolute; left: 22px; top: 1044px;
    font-family: "Noto Serif JP", serif; font-size: 20px; color: var(--green);
  }
  .footer-band {
    position: absolute; left: 0; top: 1074px; width: 849px; height: 90px; background: var(--green);
  }
  .footer-title {
    position: absolute; left: 22px; top: 6px;
    font-family: "Noto Serif JP", serif; font-weight: 600; font-size: 32px; line-height: 1.2; color: var(--white);
  }
  .phone {
    position: absolute; left: 372px; top: 8px; display: flex; align-items: center; gap: 6px;
    font-family: "Noto Serif JP", serif; font-weight: 700; font-size: 36px; color: var(--white);
  }
  .phone svg { width: 30px; height: 30px; }
  .hours {
    position: absolute; left: 376px; top: 56px; font-size: 13px; color: var(--white);
  }
  .shop-badge {
    position: absolute; right: 22px; top: 44px; width: 96px; height: 40px;
    border: 2px solid var(--white); background: var(--green-dark);
    color: var(--white); font-size: 11px; display: flex; align-items: center; justify-content: center;
  }
  .payment-note {
    position: absolute; left: 22px; top: 1170px; font-size: 11px; color: var(--text);
  }
</style>
</head>
<body>
<div class="flyer">
  <div class="hero-photo" role="img" aria-label="エプロン姿のスタッフが室内を掃除している写真"></div>
  <p class="hero-lead">暮らしの困った…</p>
  <h1 class="hero-title">そよかぜ<br>クリーンサービス</h1>

  <div class="bubble bubble--memorial">
    <p class="heading">〜遺品の整理〜</p>
    <p>思い出が詰まった大切な遺品、<br>当社が丁寧に整理致します。<br>その他遺品に関するお悩み<br>ご相談承ります。</p>
  </div>
  <div class="bubble bubble--home">
    <p class="heading">〜暮らしのお片付け〜</p>
    <p class="bubble-items">・ゴミ屋敷をピカピカに!<br>・ベランダのお掃除!<br>・不用品の処分!</p>
  </div>
  <div class="bubble bubble--storage">
    <p class="heading">〜トランクルームのお片付け〜</p>
    <p>お荷物を指定の場所まで<br>お運びします!<br>もちろん不用品処分<br>承ります!</p>
  </div>
  <div class="bubble bubble--more">
    <p>ほかにも…<br>〜リフォーム〜<br>〜高価買取〜<br>〜電気の困った〜</p>
  </div>

  <p class="message">まずはお電話でお見積を!よろしければその日にお伺いします。<br>どんなことでもお気軽に御相談下さい。<br>お電話お待ちしております。</p>

  <p class="company">(株) グリーンフィールド</p>
  <div class="footer-band">
    <p class="footer-title">そよかぜ<br>クリーンサービス</p>
    <p class="phone">
      <svg viewBox="0 0 24 24" aria-hidden="true"><path fill="#ffffff" d="M6.6 10.8a15.1 15.1 0 0 0 6.6 6.6l2.2-2.2a1 1 0 0 1 1-.25 11.4 11.4 0 0 0 3.6.57 1 1 0 0 1 1 1V20a1 1 0 0 1-1 1A17 17 0 0 1 3 4a1 1 0 0 1 1-1h3.5a1 1 0 0 1 1 1c0 1.25.2 2.45.57 3.57a1 1 0 0 1-.25 1z"/></svg>
      00-0000-0000
    </p>
    <p class="hours">お電話受付 AM 9:00 ~ PM 8:00　定休日 日曜日</p>
    <div class="shop-badge">店舗をチェック</div>
  </div>
  <p class="payment-note">各種クレジットカード使えます　主要クレジットカード・各種電子マネー</p>
</div>
</body>
</html>
```